Coming Soon page for a new fitness startup

We are a new startup based in Toronto, Canada working on a site and mobile app where people can register for athletic events such as running, cycling, triathlon, SUP, etc.

Participants will also be able to manage their clubs and team, and connect their fitness trackers so they have all their fitness data and friends in one place.

I like very simple designs and lots of whitespace. So no need for icons or unnecessary graphics.

I prefer having a mobile phone app instead of a hero image. No need to worry about the details within the mobile app for now, we can fill it in later. Here are some landing pages that I like.
https://pixelshelf.example/tormundlaksa/buckets/493817-Landing-Page

Attached is a wireframe that gives some sample content for each of the sections. Please do not take the wireframe too literally, it is only meant to illustrate the content that we are experimenting with and should give an idea of how much text will be on the page.

I have also attached the company logo files. The logo is not being used yet so feel free to simplify the logo if it doesn't look great with your design. For example, I'm ok with just the name "vexqari" in white if that looks better.

Target Market(s)

Ages 25 to 45. Interested in running, cycling, triathlon, SUP, etc.

Industry/Entity Type

Fitness

Coding

Coded - Design and coding required

Number of Pages Required

1 page

Requirements
Should not have
• Any photos should not contain track and field events, or people in a gym. Any photos should have people running or cycling outdoors. I know that photos can be easily swapped out but it is distracting to review a design that has the wrong photos.

```html
<!DOCTYPE html>
<html lang="en">
<head>
<meta charset="utf-8">
<title>vexqari — Coming Soon</title>
<link rel="stylesheet" href="https://fonts.googleapis.com/css2?family=Open+Sans:ital,wght@0,400;0,600;0,700;1,400&family=Raleway:wght@500;600;700&display=swap">
<style>
  :root {
    --red: #d7232f;
    --ink: #2b2b2b;
    --muted: #6d6d6d;
    --line: #bfbfbf;
    --white: #ffffff;
    --footer: #2a2d2c;
  }
  * { box-sizing: border-box; margin: 0; padding: 0; }
  html, body { width: 833px; height: 1200px; overflow: hidden; background: var(--white); }
  body { position: relative; font-family: "Open Sans", sans-serif; color: var(--ink); }

  .hero { position: absolute; left: 0; top: 0; width: 833px; height: 410px; overflow: hidden; }
  .hero-photo {
    position: absolute; inset: 0;
    background:
      radial-gradient(ellipse at 40% 20%, rgba(120,110,60,.55), transparent 55%),
      radial-gradient(ellipse at 85% 10%, rgba(90,30,25,.7), transparent 50%),
      linear-gradient(160deg, #5e5a2c 0%, #3c3421 35%, #3b2e2a 60%, #5b5352 100%);
  }
  .brand { position: absolute; left: 69px; top: 32px; display: flex; align-items: center; gap: 8px;
    font-family: "Raleway", sans-serif; font-weight: 600; font-size: 30px; color: var(--white); }
  .brand-dot { width: 34px; height: 34px; border: 2px solid var(--white); border-radius: 50%; }
  .menu-btn { position: absolute; left: 733px; top: 32px; width: 30px; height: 30px; border-radius: 50%; background: var(--red); }
  .menu-btn span { position: absolute; left: 8px; width: 14px; height: 2px; background: var(--white); border-radius: 1px; }

  .hero-copy { position: absolute; left: 398px; top: 112px; width: 400px; color: var(--white); }
  .hero-copy h1 { font-family: "Raleway", sans-serif; font-weight: 600; font-size: 27px; line-height: 33px; }
  .hero-copy .lead { margin-top: 13px; font-size: 11.2px; line-height: 18.4px; width: 360px; }
  .hero-copy .invite { margin-top: 13px; font-style: italic; font-size: 13px; line-height: 19.5px; width: 360px; }
  .notify { position: absolute; left: 399px; top: 318px; display: flex; }
  .notify input { width: 262px; height: 34px; border: 0; padding: 0 15px; font: 400 10.5px "Open Sans", sans-serif; color: var(--muted); background: var(--white); }
  .notify button { width: 93px; height: 34px; border: 0; background: var(--red); color: var(--white); font: 700 11px "Open Sans", sans-serif; letter-spacing: .3px; }

  .phone { position: absolute; left: 70px; top: 124px; width: 159px; height: 322px; border-radius: 20px;
    background: #f2f2f2; border: 2px solid #d6d6d6; box-shadow: 0 2px 6px rgba(0,0,0,.2); }
  .phone .speaker { position: absolute; left: 70px; top: 16px; width: 20px; height: 1.5px; background: #333; }
  .phone .camera { position: absolute; left: 55px; top: 15px; width: 4px; height: 4px; border-radius: 50%; background: #333; }
  .phone .screen { position: absolute; left: 7px; top: 33px; width: 143px; height: 252px; background: #000;
    display: flex; align-items: center; justify-content: center;
    font-family: "Raleway", sans-serif; font-weight: 600; font-size: 30px; color: var(--white); }
  .phone .home { position: absolute; left: 68px; top: 292px; width: 20px; height: 20px; border-radius: 50%; border: 1px solid #444; }

  .features { position: absolute; left: 0; top: 490px; width: 833px; text-align: center; }
  .features h2 { font-family: "Raleway", sans-serif; font-weight: 600; font-size: 22.5px; color: var(--ink); }
  .features .sub { margin-top: 12px; font-size: 13px; color: #555; }
  .cards { position: absolute; left: 69px; top: 102px; display: flex; gap: 23px; }
  .card { width: 217px; height: 210px; border: 1px solid var(--line); text-align: center; padding-top: 19px; }
  .card svg { display: block; margin: 0 auto; }
  .card h3 { margin-top: 29px; font-family: "Raleway", sans-serif; font-weight: 600; font-size: 15px; color: var(--ink); }
  .card p { margin: 15px auto 0; width: 190px; font-size: 9.8px; line-height: 18px; color: var(--muted); }

  .organize { position: absolute; left: 0; top: 870px; width: 833px; height: 276px; overflow: hidden; color: var(--white); }
  .organize-photo { position: absolute; inset: 0;
    background:
      radial-gradient(ellipse at 30% 60%, rgba(110,150,140,.6), transparent 55%),
      linear-gradient(120deg, #5d5a44 0%, #4a5a52 35%, #3c4a42 60%, #585a4a 100%); }
  .organize-copy { position: absolute; left: 69px; top: 53px; width: 350px; }
  .organize-copy h2 { font-family: "Raleway", sans-serif; font-weight: 600; font-size: 22px; }
  .organize-copy p { font-size: 10.3px; line-height: 17.5px; }
  .organize-copy .first { margin-top: 16px; }
  .organize-copy .second { margin-top: 16px; }
  .organize-copy a { display: inline-block; margin-top: 17px; font-size: 10.5px; font-weight: 600; color: var(--white); text-decoration: underline; letter-spacing: .2px; }
  .contact { position: absolute; left: 461px; top: 40px; width: 303px; }
  .contact h3 { font-family: "Raleway", sans-serif; font-weight: 600; font-size: 14.5px; }
  .contact input, .contact textarea { display: block; width: 303px; border: 0; background: var(--white); padding: 0 10px;
    font: 400 8.5px "Open Sans", sans-serif; color: var(--muted); resize: none; }
  .contact input { height: 22px; margin-top: 9px; }
  .contact .name { margin-top: 16px; }
  .contact textarea { height: 56px; margin-top: 9px; padding-top: 10px; }
  .contact button { display: block; margin: 10px 0 0 auto; width: 62px; height: 27px; border: 0; background: var(--red); color: var(--white); font: 700 9.5px "Open Sans", sans-serif; }

  .footer { position: absolute; left: 0; top: 1146px; width: 833px; height: 54px; background: var(--footer); color: var(--white); font-size: 9px; }
  .footer nav { position: absolute; left: 69px; top: 20px; }
  .footer nav a { color: var(--white); text-decoration: none; }
  .footer nav .sep { margin: 0 7px; }
  .social { position: absolute; left: 369px; top: 14px; display: flex; gap: 8px; }
  .social span { width: 26px; height: 26px; border: 1px solid var(--white); border-radius: 50%; }
  .copyright { position: absolute; right: 71px; top: 20px; }
</style>
</head>
<body>
  <header class="hero">
    <div class="hero-photo" role="img" aria-label="Photo of a cyclist riding a road bike outdoors on a tree-lined road"></div>
    <div class="brand"><span class="brand-dot"></span>vexqari</div>
    <div class="menu-btn" aria-label="Menu"><span style="top:10px"></span><span style="top:14px"></span><span style="top:18px"></span></div>
    <div class="hero-copy">
      <h1>Connect your training, friends, and events in one place</h1>
      <p class="lead">Nam libero tempore, cum soluta nobis est eligendi optio cumquenihil impedit quo minus id quod maxime placeat facere possimus, omnivol uptas assumenda est, omnis dolor repellendus.</p>
      <p class="invite">Join our email list. A referral program is coming and you'll want to be the first to know</p>
    </div>
    <form class="notify"><input type="email" placeholder="Email Address"><button type="button">NOTIFY ME</button></form>
  </header>

  <div class="phone">
    <span class="camera"></span><span class="speaker"></span>
    <div class="screen">vexqari</div>
    <span class="home"></span>
  </div>

  <section class="features">
    <h2>Training and Racing all in one place</h2>
    <p class="sub">A new fitness community is coming soon</p>
    <div class="cards">
      <article class="card">
        <svg width="40" height="40" viewBox="0 0 40 40" aria-hidden="true">
          <rect x="3" y="6" width="34" height="31" rx="2" fill="none" stroke="var(--red)" stroke-width="3"/>
          <rect x="3" y="6" width="34" height="7" fill="var(--red)"/>
          <rect x="10" y="2" width="3" height="8" fill="var(--red)"/><rect x="27" y="2" width="3" height="8" fill="var(--red)"/>
          <g stroke="var(--red)" stroke-width="1.5"><path d="M3 19h34M3 25h34M3 31h34M10 13v24M17 13v24M23 13v24M30 13v24"/></g>
        </svg>
        <h3>Find Events</h3>
        <p>At vero eos et accusamus et iusto odio dignissimos ducimus qui blanditiis praese nti um voluptatum deleniti atque corrupti qu os dolores et quas molestia</p>
      </article>
      <article class="card">
        <svg width="44" height="40" viewBox="0 0 44 40" aria-hidden="true" fill="var(--red)">
          <circle cx="9" cy="10" r="6"/><circle cx="35" cy="10" r="6"/><circle cx="22" cy="12" r="7.5"/>
          <path d="M0 28c0-6 4-9 9-9s6 2 6 2c-3 3-4 6-4 9H0z"/><path d="M44 28c0-6-4-9-9-9s-6 2-6 2c3 3 4 6 4 9h11z"/>
          <path d="M10 38c0-9 5-14 12-14s12 5 12 14z"/>
        </svg>
        <h3>Invite your friends</h3>
        <p>At vero eos et accusamus et iusto odio dignissimos ducimus qui blanditiis praese nti um voluptatum deleniti atque corrupti qu os dolores et quas molestia</p>
      </article>
      <article class="card">
        <svg width="40" height="40" viewBox="0 0 40 40" aria-hidden="true" fill="none" stroke="var(--red)" stroke-width="4.5">
          <rect x="3" y="5" width="16" height="12" rx="6" transform="rotate(45 11 11)"/>
          <rect x="21" y="23" width="16" height="12" rx="6" transform="rotate(45 29 29)"/>
          <path d="M15 15l10 10"/>
        </svg>
        <h3>Connect your workouts</h3>
        <p>At vero eos et accusamus et iusto odio dignissimos ducimus qui blanditiis praese nti um voluptatum deleniti atque corrupti qu os dolores et quas molestia</p>
      </article>
    </div>
  </section>

  <section class="organize">
    <div class="organize-photo" role="img" aria-label="Photo of a runner outdoors wearing headphones and checking her phone"></div>
    <div class="organize-copy">
      <h2>Organizing an event?</h2>
      <p class="first">Attracting participants is hard.</p>
      <p class="second">With your event listed on vexqari well not not only handle the registration and payment process, we've also mode it our own personal mission to drive up participation numbers across all events.</p>
      <a href="#">CONTACT US TO LEARN MORE</a>
    </div>
    <form class="contact">
      <h3>We'd love to hear from you</h3>
      <input class="name" type="text" placeholder="Your name :">
      <input type="email" placeholder="Email Address:">
      <textarea placeholder="How can we help?"></textarea>
      <button type="button">SEND</button>
    </form>
  </section>

  <footer class="footer">
    <nav><a href="#">About us</a><span class="sep">|</span><a href="#">Developers</a><span class="sep">|</span><a href="#">Careers</a></nav>
    <div class="social"><span></span><span></span><span></span></div>
    <p class="copyright">Copyright © 2018, Vexqari. All rights reserved.</p>
  </footer>
</body>
</html>
```